Young a vibrant Letting agent. New approach to the old market. our colors are various shades of green. We want a clean and clear design with our logo and beautiful shapes. Not too crowded but not too empty. Surprise us!

Size A5, (A4 folded in two)-Cover-Page2-Page3-Back Cover

Once the first and last page is designed, i will send you the content for page 2 and 3

```html
<!DOCTYPE html>
<html lang="en">
<head>
<meta charset="utf-8">
<title>Kelso Lettings – A5 Brochure Presentation</title>
<link rel="stylesheet" href="https://fonts.googleapis.com/css2?family=Open+Sans:wght@400;600;700;800&display=swap">
<style>
:root{
  --backdrop:#3b3b3b;
  --paper:#ffffff;
  --green:#5fa823;
  --green-light:#9ed23e;
  --green-deep:#2e7a1c;
  --green-dark:#173d17;
  --ink-green:#3b8a1f;
  --ink-grey:#9a9a9a;
  --label:#f2f2f2;
}
*{box-sizing:border-box;margin:0;padding:0}
html,body{width:1200px;height:600px;overflow:hidden}
body{background:var(--backdrop);font-family:"Open Sans",Arial,sans-serif;position:relative}
.board{position:relative;width:1200px;height:600px}
.label{position:absolute;color:var(--label);font-weight:700;font-size:17px;line-height:1.15;letter-spacing:.2px}
.page{position:absolute;background:var(--paper);overflow:hidden;box-shadow:0 2px 6px rgba(0,0,0,.45)}
.spread .fold{position:absolute;top:0;bottom:0;left:50%;width:1px;background:rgba(0,0,0,.06)}
.leaf{position:absolute;background:linear-gradient(180deg,var(--green-light),var(--green) 70%,var(--green-deep));border-radius:0 16px 0 16px;box-shadow:inset 0 2px 3px rgba(0,0,0,.35),0 1px 1px rgba(0,0,0,.15)}
.leaf.flip{border-radius:16px 0 16px 0}
.leaf.dark{background:linear-gradient(180deg,#2a5a24,var(--green-dark))}
.brand-box{position:absolute;background:var(--paper);box-shadow:0 1px 4px rgba(0,0,0,.4);display:flex;align-items:center;justify-content:center;text-align:center;color:var(--green-dark);font-weight:800;line-height:1.05}
.brand-inline{position:absolute;color:var(--green-dark);font-weight:800;font-size:5px;text-align:right}
.contact{position:absolute;right:6%;color:#fff;font-size:3.6px;font-weight:600;text-align:right;line-height:1.5}
.banner{position:absolute;left:0;color:#fff;font-weight:600;padding:3% 6% 3% 5%;border-radius:0 0 18px 0;background:linear-gradient(90deg,var(--green-deep),var(--green) 60%,var(--green-light));box-shadow:inset 0 -2px 3px rgba(0,0,0,.2)}
.banner.intro{font-size:5px;line-height:1.3}
.banner.heading{font-size:9px;display:flex;align-items:center;justify-content:center;border-radius:0 18px 0 18px}
.copy{position:absolute;left:4%;right:4%;font-size:3.6px;line-height:1.35;color:var(--ink-green);font-weight:600}
.copy.grey{color:var(--ink-grey);font-weight:400}
.copy.col{left:47%}
.photo{position:absolute;left:4%;width:40%;height:21%}
.photo.lounge{background:linear-gradient(180deg,#c9cfc8 0%,#9da49b 55%,#6e6a60 100%)}
.photo.room{background:linear-gradient(180deg,#e0dccf 0%,#c8bda5 55%,#8f8068 100%)}
.strapline{position:absolute;left:3%;color:#fff;font-size:3.3px;line-height:1.3;font-weight:600}
.web{position:absolute;left:5%;color:#fff;font-size:4px;font-weight:700}
.type-strip{position:absolute;background:linear-gradient(180deg,var(--green-light),var(--green) 50%,var(--green-deep));opacity:.9}
</style>
</head>
<body>
<main class="board">

  <!-- Option 1 cover -->
  <div class="label" style="left:32px;top:32px">Option 1 Page 1</div>
  <section class="page cover" style="left:21px;top:60px;width:146px;height:210px">
    <div class="leaf" style="left:0;top:5%;width:88%;height:13%"></div>
    <div class="leaf" style="left:0;top:20%;width:62%;height:7%"></div>
    <div class="brand-box" style="left:52%;top:35%;width:32%;height:20%;font-size:8px">Kelso Lettings</div>
    <div class="leaf" style="left:0;top:62%;width:70%;height:9%"></div>
    <div class="leaf" style="left:0;top:73%;width:92%;height:13%"></div>
    <div class="leaf" style="left:0;top:88%;width:84%;height:9%"></div>
  </section>

  <!-- Page 2 -->
  <div class="label" style="left:244px;top:32px">Page 2</div>
  <section class="page inner" style="left:196px;top:58px;width:153px;height:212px">
    <div class="banner intro" style="top:2%;width:90%;height:22%">By choosing Kelso Lettings to market your property, you choose to save money. We, unlike other agents, work on a no let-no fee basis, and do not charge for marketing your property.</div>
    <p class="copy" style="top:26%">Instructing us to market your property would cost you nothing and you would only pay if the property is let by us. If you let it through other agent, we won't charge you a penny.</p>
    <div class="photo lounge" style="top:38%" role="img" aria-label="Photo of a bright living room with a fireplace"></div>
    <p class="copy col" style="top:38%">We will attend viewings 7 days from 8am until 9pm, as most tenants are working during the day and would find very convenient evening and weekends appointments</p>
    <p class="copy grey" style="top:62%">We will carefully choose a suitable tenant, do all referencing, credit checks and employment referencing. We would present you all information we have and it is your decision</p>
    <p class="copy" style="top:74%">If the property is let by us, once the tenancy agreement is signed, we would charge you a fee of £250+VAT.</p>
    <div class="leaf dark" style="left:0;top:83%;width:64%;height:9%"></div>
    <p class="strapline" style="top:84.5%;width:58%">No percentage, no complicated contracts. No fee basis, and we do not charge for marketing your property</p>
    <div class="brand-inline" style="right:5%;top:87%">Kelso Lettings</div>
    <div class="leaf" style="left:0;top:93.5%;width:52%;height:5%"></div>
    <div class="web" style="top:94%">www.kelsolets.co.uk</div>
  </section>

  <!-- Option 2 cover -->
  <div class="label" style="left:26px;top:314px">Option 2 Page 1</div>
  <section class="page cover" style="left:16px;top:342px;width:155px;height:222px">
    <div class="leaf" style="left:0;top:4%;width:74%;height:11%"></div>
    <div class="leaf" style="left:0;top:17%;width:54%;height:7%"></div>
    <div class="brand-box" style="left:20%;top:37%;width:38%;height:20%;font-size:9px">Kelso Lettings</div>
    <div class="leaf" style="left:0;top:63%;width:68%;height:10%"></div>
    <div class="leaf" style="left:0;top:75%;width:74%;height:11%"></div>
    <div class="leaf" style="left:0;top:88%;width:62%;height:9%"></div>
    <div class="type-strip" style="left:85%;top:2%;width:13%;height:95%" role="img" aria-label="Decorative stack of the word Lettings in mixed green type"></div>
  </section>

  <!-- Page 3 -->
  <div class="label" style="left:244px;top:307px">Page 3</div>
  <section class="page inner" style="left:196px;top:342px;width:153px;height:221px">
    <div class="banner heading" style="top:4%;width:92%;height:17%">Info for page 3</div>
    <p class="copy" style="top:24%">Instructing us to market your property would cost you nothing and you would only pay if the property is let by us. If you let it through other agent, we won't charge you a penny.</p>
    <div class="photo room" style="top:36%" role="img" aria-label="Photo of a light furnished lounge"></div>
    <p class="copy col" style="top:36%">We will attend viewings 7 days from 8am until 9pm, as most tenants are working during the day and would find very convenient evening and weekends appointments</p>
    <p class="copy grey" style="top:62%">We will carefully choose a suitable tenant, do all referencing, credit checks and employment referencing. We would present you all information we have and it is your decision</p>
    <div class="leaf dark" style="left:0;top:84%;width:64%;height:8%"></div>
    <p class="strapline" style="top:85.5%;width:58%">No fee basis, and we do not charge for marketing your property</p>
    <div class="brand-inline" style="right:5%;top:87%">Kelso Lettings</div>
    <div class="leaf" style="left:0;top:93.5%;width:52%;height:5%"></div>
    <div class="web" style="top:94%">www.kelsolets.co.uk</div>
  </section>

  <!-- Page 4 -->
  <div class="label" style="left:409px;top:307px">Page 4</div>
  <section class="page back" style="left:361px;top:342px;width:153px;height:221px">
    <div class="leaf flip" style="right:0;left:auto;top:64%;width:86%;height:11%"></div>
    <p class="contact" style="top:65.5%">Northfield: 01632 960277<br>London: 020 7946 0318</p>
    <div class="leaf flip" style="right:0;left:auto;top:77%;width:66%;height:8%"></div>
    <div class="leaf flip" style="right:0;left:auto;top:87%;width:90%;height:11%"></div>
    <p class="contact" style="top:89%">Email: lettings@kelsolets.co.uk<br>www.kelsolets.co.uk</p>
  </section>

  <!-- Exterior option 1 -->
  <div class="label" style="left:577px;top:370px">Exterior<br>&nbsp;option 1</div>
  <section class="page spread" style="left:577px;top:421px;width:243px;height:175px">
    <div class="fold"></div>
    <div class="leaf" style="left:0;top:3%;width:37%;height:13%"></div>
    <div class="leaf" style="left:0;top:18%;width:28%;height:8%"></div>
    <div class="brand-box" style="left:25%;top:38%;width:18%;height:21%;font-size:7px">Kelso Lettings</div>
    <div class="leaf" style="left:0;top:63%;width:33%;height:11%"></div>
    <div class="leaf" style="left:0;top:77%;width:37%;height:12%"></div>
    <div class="leaf" style="left:0;top:91%;width:28%;height:7%"></div>
    <div class="leaf flip" style="left:auto;right:0;top:64%;width:47%;height:10%"></div>
    <p class="contact" style="top:65.5%;right:3%">Northfield: 01632 960277<br>London: 020 7946 0318</p>
    <div class="leaf flip" style="left:auto;right:0;top:77%;width:34%;height:8%"></div>
    <div class="leaf flip" style="left:auto;right:0;top:88%;width:47%;height:10%"></div>
    <p class="contact" style="top:89.5%;right:3%">Email: lettings@kelsolets.co.uk<br>www.kelsolets.co.uk</p>
  </section>

  <!-- Interior spread -->
  <div class="label" style="left:742px;top:58px">Interior</div>
  <section class="page spread" style="left:850px;top:13px;width:333px;height:220px">
    <div class="fold"></div>
    <div class="inner" style="position:absolute;left:0;top:0;width:50%;height:100%">
      <div class="banner intro" style="top:2%;width:90%;height:20%">By choosing Kelso Lettings to market your property, you choose to save money. We, unlike other agents, work on a no let-no fee basis, and do not charge for marketing your property.</div>
      <p class="copy" style="top:25%">Instructing us to market your property would cost you nothing and you would only pay if the property is let by us. If you let it through other agent, we won't charge you a penny.</p>
      <div class="photo lounge" style="top:37%" role="img" aria-label="Photo of a bright living room with a fireplace"></div>
      <p class="copy col" style="top:37%">We will attend viewings 7 days from 8am until 9pm, as most tenants are working during the day and would find very convenient evening and weekends appointments</p>
      <p class="copy grey" style="top:61%">We will carefully choose a suitable tenant, do all referencing, credit checks and employment referencing. We would present you all information we have and it is your decision</p>
      <p class="copy" style="top:73%">If the property is let by us, once the tenancy agreement is signed, we would charge you a fee of £250+VAT.</p>
      <div class="leaf dark" style="left:0;top:84%;width:62%;height:8%"></div>
      <p class="strapline" style="top:85.5%;width:56%">No percentage, no complicated contracts. No fee basis, and we do not charge for marketing your property</p>
      <div class="brand-inline" style="right:5%;top:88%">Kelso Lettings</div>
      <div class="leaf" style="left:0;top:93.5%;width:48%;height:5%"></div>
      <div class="web" style="top:94%">www.kelsolets.co.uk</div>
    </div>
    <div class="inner" style="position:absolute;left:50%;top:0;width:50%;height:100%">
      <div class="banner heading" style="top:4%;width:92%;height:17%">Info for page 3</div>
      <p class="copy" style="top:25%">Instructing us to market your property would cost you nothing and you would only pay if the property is let by us. If you let it through other agent, we won't charge you a penny.</p>
      <div class="photo room" style="top:37%" role="img" aria-label="Photo of a light furnished lounge"></div>
      <p class="copy col" style="top:37%">We will attend viewings 7 days from 8am until 9pm, as most tenants are working during the day and would find very convenient evening and weekends appointments</p>
      <p class="copy grey" style="top:62%">We will carefully choose a suitable tenant, do all referencing, credit checks and employment referencing. We would present you all information we have and it is your decision</p>
      <div class="leaf dark" style="left:0;top:84%;width:62%;height:8%"></div>
      <p class="strapline" style="top:85.5%;width:56%">No fee basis, and we do not charge for marketing your property</p>
      <div class="brand-inline" style="right:5%;top:88%">Kelso Lettings</div>
      <div class="leaf" style="left:0;top:93.5%;width:48%;height:5%"></div>
      <div class="web" style="top:94%">www.kelsolets.co.uk</div>
    </div>
  </section>

  <!-- Exterior option 2 -->
  <div class="label" style="left:742px;top:256px">Exterior<br>&nbsp;option 2</div>
  <section class="page spread" style="left:849px;top:252px;width:311px;height:224px">
    <div class="fold"></div>
    <div class="leaf" style="left:0;top:3%;width:26%;height:12%"></div>
    <div class="leaf" style="left:0;top:18%;width:19%;height:7%"></div>
    <div class="brand-box" style="left:10%;top:36%;width:16%;height:20%;font-size:8px">Kelso Lettings</div>
    <div class="leaf" style="left:0;top:65%;width:28%;height:10%"></div>
    <div class="leaf" style="left:0;top:77%;width:34%;height:11%"></div>
    <div class="leaf" style="left:0;top:90%;width:26%;height:8%"></div>
    <div class="type-strip" style="left:38%;top:2%;width:6%;height:96%" role="img" aria-label="Decorative stack of the word Lettings in mixed green type"></div>
    <div class="leaf flip" style="left:auto;right:0;top:58%;width:43%;height:10%"></div>
    <p class="contact" style="top:59.5%;right:3%">Northfield: 01632 960277<br>London: 020 7946 0318</p>
    <div class="leaf flip" style="left:auto;right:0;top:71%;width:28%;height:8%"></div>
    <div class="leaf flip" style="left:auto;right:0;top:83%;width:45%;height:11%"></div>
    <p class="contact" style="top:85%;right:3%">Email: lettings@kelsolets.co.uk<br>www.kelsolets.co.uk</p>
  </section>

</main>
</body>
</html>
```